TITLE: What Lifts a Young Player Past the Bench? SUB-TITLE: A Family’s Plain Talk Manual for Coaching...

My book is for parents who have young children that are really into sports. My book empowers parents so they can motivate their children to succeed. It deals with sports psychology. Both my title and subtitle should be easy to read. Ideally, I would like a picture of young athlete(s) on the title. I have uploaded files of some books on Brindlemart that deal with the same subject. The last two files are 1) my company logo, please try to include these colors 2) an ebook cover I put together myself. You will notice an On-line bonus in the middle of the book, this Bonus needs to be on the cover.

Target Market(s)

Parents with children who play sports at a high level

Colors

Designer to choose colors to be used in the design.

Requirements
Must have
• Online Bonus feature as per my example.
• Dimensions: Paperlyn = The ideal size of your eBook cover art is a height/width ratio of 1.6:1. This means that for every 1,000 pixels in width, the image should be 1,600 pixels in height.
Nice to have
• picture of a young athlete or young athletes

```html
<!DOCTYPE html>
<html lang="en">
<head>
<meta charset="utf-8">
<title>What Lifts a Young Player Past the Bench?</title>
<link rel="stylesheet" href="https://fonts.googleapis.com/css2?family=Orbitron:wght@700;900&family=Roboto+Condensed:wght@700&display=swap">
<style>
  :root {
    --ink: #000000;
    --paper: #ffffff;
    --accent: #f7941d;
    --gold-light: #ffe58a;
    --gold: #e8b330;
    --gold-deep: #b8801a;
    --badge-text: #2a1a05;
  }
  html, body {
    margin: 0;
    padding: 0;
    overflow: hidden;
    background: var(--ink);
  }
  .cover {
    position: relative;
    width: 750px;
    height: 1200px;
    background: var(--ink);
    overflow: hidden;
    font-family: "Orbitron", sans-serif;
  }
  .subtitle {
    position: absolute;
    top: 40px;
    left: 0;
    width: 100%;
    margin: 0;
    text-align: center;
    color: var(--accent);
    font-family: "Orbitron", sans-serif;
    font-weight: 700;
    font-size: 19.5px;
    line-height: 29px;
    text-transform: uppercase;
    letter-spacing: 0.2px;
  }
  .athlete-strip {
    position: absolute;
    top: 130px;
    left: 0;
    width: 750px;
    height: 270px;
    display: flex;
  }
  .athlete-panel {
    flex: 1;
    height: 100%;
  }
  .panel-rings { background: linear-gradient(180deg, #2f4a5c, #1c2d3a 60%, #3b5564); }
  .panel-racket { background: linear-gradient(160deg, #060606, #142a2a 60%, #0a0a0a); }
  .panel-hockey { background: linear-gradient(180deg, #1f3347, #3f5d78 60%, #c9d6e0); }
  .panel-soccer { background: linear-gradient(180deg, #1b2a3c, #3a4e3a 55%, #3c6b2a); }
  .panel-ribbon { background: linear-gradient(180deg, #f2f2f2, #e4e4e4 70%, #d8d8d8); }
  .panel-karate { background: linear-gradient(180deg, #0f2c6a, #1e4c9c 55%, #0f2a5c); }
  .panel-skating { background: linear-gradient(180deg, #3a4f63, #8b9eb0 60%, #dfe6ec); }
  .title {
    position: absolute;
    top: 452px;
    left: 0;
    width: 100%;
    margin: 0;
    text-align: center;
    color: var(--paper);
    font-family: "Orbitron", sans-serif;
    font-weight: 900;
    text-transform: uppercase;
  }
  .title-lead {
    display: block;
    font-size: 40px;
    line-height: 60px;
    letter-spacing: 0.5px;
  }
  .title-main {
    display: block;
    font-size: 92px;
    line-height: 104px;
    letter-spacing: -1px;
  }
  .bonus-seal {
    position: absolute;
    left: 298px;
    top: 886px;
    width: 156px;
    height: 156px;
  }
  .bonus-seal text {
    font-family: "Roboto Condensed", sans-serif;
    font-weight: 700;
    fill: var(--badge-text);
    text-anchor: middle;
  }
  .author-band {
    position: absolute;
    left: 0;
    top: 1088px;
    width: 750px;
    height: 112px;
    background: var(--paper);
  }
  .author-name {
    position: absolute;
    left: 40px;
    top: 0;
    margin: 0;
    line-height: 112px;
    font-family: "Orbitron", sans-serif;
    font-weight: 900;
    font-size: 50px;
    letter-spacing: -0.5px;
    color: var(--ink);
    text-transform: uppercase;
  }
  .studio-mark {
    position: absolute;
    right: 26px;
    top: 26px;
    width: 80px;
    display: flex;
    flex-direction: column;
    align-items: center;
    gap: 6px;
  }
  .studio-dot {
    width: 34px;
    height: 34px;
    border-radius: 50%;
    background: var(--accent);
  }
  .studio-name {
    font-family: "Orbitron", sans-serif;
    font-weight: 700;
    font-size: 11px;
    color: var(--accent);
    text-transform: uppercase;
    white-space: nowrap;
  }
</style>
</head>
<body>
<main class="cover">
  <p class="subtitle">A Family’s Plain Talk Manual<br>for Coaching...</p>

  <div class="athlete-strip">
    <div class="athlete-panel panel-rings" role="img" aria-label="Young gymnast holding a pose on the still rings"></div>
    <div class="athlete-panel panel-racket" role="img" aria-label="Young player swinging a racket with light trails on a dark background"></div>
    <div class="athlete-panel panel-hockey" role="img" aria-label="Young ice hockey player skating with a stick"></div>
    <div class="athlete-panel panel-soccer" role="img" aria-label="Young soccer player kicking a ball on a stadium pitch"></div>
    <div class="athlete-panel panel-ribbon" role="img" aria-label="Young rhythmic gymnast with a ribbon in a high leg hold"></div>
    <div class="athlete-panel panel-karate" role="img" aria-label="Young martial artist in a white uniform performing a kick"></div>
    <div class="athlete-panel panel-skating" role="img" aria-label="Young figure skater in a white dress posing on ice"></div>
  </div>

  <h1 class="title">
    <span class="title-lead">What Lifts a Young</span>
    <span class="title-main">Player</span>
    <span class="title-main">Past The</span>
    <span class="title-main">Bench?</span>
  </h1>

  <svg class="bonus-seal" viewBox="0 0 160 160" aria-label="Free online workshop, $170 value, details inside">
    <defs>
      <radialGradient id="sealGold" cx="40%" cy="35%" r="70%">
        <stop offset="0" stop-color="var(--gold-light)"/>
        <stop offset="0.55" stop-color="var(--gold)"/>
        <stop offset="1" stop-color="var(--gold-deep)"/>
      </radialGradient>
    </defs>
    <polygon fill="url(#sealGold)" points="80,2 87,12 98,4 102,16 114,11 115,23 128,22 125,34 138,36 132,47 144,53 135,62 145,70 134,77 142,87 130,92 135,104 122,106 124,119 112,118 111,131 99,127 95,139 85,132 80,143 75,132 65,139 61,127 49,131 48,118 36,119 38,106 25,104 30,92 18,87 26,77 15,70 25,62 16,53 28,47 22,36 35,34 32,22 45,23 46,11 58,16 62,4 73,12"/>
    <circle cx="80" cy="73" r="54" fill="none" stroke="var(--gold-deep)" stroke-width="1.5" opacity="0.6"/>
    <text x="80" y="55" font-size="17">FREE</text>
    <text x="80" y="73" font-size="17">ONLINE</text>
    <text x="80" y="91" font-size="17">WORKSHOP</text>
    <text x="80" y="109" font-size="17">$170 VALUE</text>
    <text x="80" y="126" font-size="10.5">Details inside</text>
  </svg>

  <footer class="author-band">
    <p class="author-name">Rafe Almonte</p>
    <div class="studio-mark">
      <span class="studio-dot"></span>
      <span class="studio-name">Mind Arena</span>
    </div>
  </footer>
</main>
</body>
</html>
```